Pell Haven Branding for Contracts and Customer facing documents

We are hoping to create a themed branding for our company. We would like to leverage this across our contracts, documents, and all client information and proposals. www.BuildWithPell.com is our website. We are selling high end custom homes. We am intending to use this template for a Lead Magnet and other marketing.

Target Market(s)

Luxury Custom Home Buyers

Industry/Entity Type

Residential Construction

Other font styles liked:
• You may choose, We want to be elegant but very legible and professional

Colors
0054AA
0677BA
7BADD7
CADEEF
E8F1F8

```html
<!DOCTYPE html>
<html lang="en">
<head>
<meta charset="utf-8">
<title>Pell Haven Custom Homes – New Client Pre-Contract Package</title>
<link rel="stylesheet" href="https://fonts.googleapis.com/css2?family=Cinzel:wght@400;600;700&family=Cormorant+Garamond:wght@500&display=swap">
<style>
  :root {
    --navy: #2b3242;
    --gold: #b08f5f;
    --paper: #ebe7e1;
    --panel: #f1f0ec;
    --cream: #f3ede3;
    --backdrop: #ececec;
  }
  * { margin: 0; padding: 0; box-sizing: border-box; }
  html, body { width: 1200px; height: 898px; overflow: hidden; background: var(--backdrop); }
  .canvas { position: relative; width: 1200px; height: 898px; }
  .sheet { position: absolute; left: 252px; top: 52px; width: 698px; height: 805px; background: var(--paper); }
  .abs { position: absolute; }
  .corner-accent { left: 775px; top: 52px; width: 175px; height: 187px; background: var(--gold); }
  .sheet-frame { left: 274px; top: 69px; width: 655px; height: 771px; border: 1px solid var(--navy); }
  .content-panel { left: 298px; top: 336px; width: 607px; height: 477px; background: var(--panel); }

  .brand-panel { left: 298px; top: 95px; width: 327px; height: 241px; background: var(--navy);
    display: flex; flex-direction: column; align-items: center; justify-content: flex-end; padding-bottom: 17px; }
  .brand-name { font-family: 'Cinzel', serif; font-weight: 400; font-size: 34px; color: var(--cream); letter-spacing: 1px; margin-bottom: 18px; }
  .brand-tagline { font-family: 'Cinzel', serif; font-weight: 700; font-size: 18px; color: var(--gold); letter-spacing: 0.5px; margin-bottom: 9px; }
  .brand-address { font-family: 'Cinzel', serif; font-weight: 600; font-size: 9.5px; color: var(--cream); }

  .photo { background: linear-gradient(180deg, #6d86a6 0%, #c9a7a4 35%, #58606c 60%, #4a6a3c 100%); }
  .photo-hero { left: 625px; top: 95px; width: 280px; height: 241px; }
  .photo-upper { left: 349px; top: 484px; width: 175px; height: 160px; }
  .photo-lower { left: 349px; top: 649px; width: 175px; height: 164px;
    background: linear-gradient(180deg, #7b94b6 0%, #4e5a6b 45%, #c79a6a 65%, #5a7d45 100%); }

  .package-band { left: 298px; top: 342px; width: 607px; height: 142px; background: var(--gold); text-align: center; }
  .package-title { position: absolute; left: 0; right: 0; top: 24px; font-family: 'Cinzel', serif; font-weight: 700;
    font-size: 24px; color: var(--navy); letter-spacing: 0.3px; padding-left: 10px; }
  .package-rule { position: absolute; left: 216px; top: 60px; width: 175px; height: 3px; background: var(--cream); }
  .package-steps { position: absolute; left: 40px; right: 40px; top: 72px; font-family: 'Cinzel', serif; font-weight: 700;
    font-size: 17px; line-height: 20px; color: var(--cream); }

  .contact-list { left: 543px; top: 555px; font-family: 'Cormorant Garamond', serif; font-weight: 500; font-size: 15px;
    color: var(--navy); letter-spacing: 0.3px; list-style: none; }
  .contact-list li { height: 45.5px; }
  .contact-divider { left: 570px; top: 697px; }

  .accent-square { left: 297px; top: 749px; width: 52px; height: 64px; background: var(--gold); }
  .footer-bar { left: 524px; top: 749px; width: 381px; height: 64px; background: var(--navy);
    display: flex; align-items: center; justify-content: center; padding-left: 30px;
    font-family: 'Cinzel', serif; font-weight: 600; font-size: 13.5px; letter-spacing: 3.2px; color: var(--cream); }
  .footer-bar .accent { color: var(--gold); margin-right: 8px; }
</style>
</head>
<body>
<main class="canvas">
  <div class="sheet"></div>
  <div class="abs corner-accent"></div>
  <div class="abs sheet-frame"></div>
  <div class="abs content-panel"></div>

  <header class="abs brand-panel">
    <div class="brand-name">Pell Haven</div>
    <div class="brand-tagline">CUSTOM HOMES</div>
    <div class="brand-address">88 ORCHARD RIDGE RD., #210 FAIRVIEW VA, 24000</div>
  </header>

  <div class="abs photo photo-hero" role="img" aria-label="Photo of a modern two-storey custom home with large lit windows at dusk"></div>

  <section class="abs package-band">
    <h1 class="package-title">NEW CLIENT PRE-CONTRACT PACKAGE</h1>
    <div class="package-rule"></div>
    <p class="package-steps">INITIAL CONSULTATION ● SITE MEETING ● DRAINFIELD EXPLORATION ● DESIGN PROCESS</p>
  </section>

  <div class="abs photo photo-upper" role="img" aria-label="Photo of a navy-sided craftsman custom home at twilight"></div>
  <div class="abs photo photo-lower" role="img" aria-label="Photo of a grey two-storey custom home with glowing windows at dusk"></div>

  <ul class="abs contact-list">
    <li>BY: DANA WHITFORD</li>
    <li>PHONE: 555-014-2290</li>
    <li>WWW.BUILDWITHPELL.COM</li>
  </ul>
  <svg class="abs contact-divider" width="96" height="8" viewBox="0 0 96 8">
    <line x1="0" y1="4" x2="96" y2="4" stroke="#2b3242" stroke-width="0.8"/>
  </svg>

  <div class="abs accent-square"></div>
  <footer class="abs footer-bar"><span class="accent">PELL HAVEN</span>CUSTOM HOMES</footer>
</main>
</body>
</html>
```